Business Card Design

Im electrician in melbourne after a business cards. I have no logos done. I have attached a card that i like but needs to be altered to my business name, so in the picture shows a lead plug into a socket spelling plug, i want the spelling replaced with my company name. I was thinking some thing with a charcoal back ground with yellow or green font.
I have wrote what I'd like above but feel free to try your own ideas and designs.
Industry/Entity Type
Electrician
Contact Information for Business Card
Zul Electrical Services PTY LTD (Display on the front of card, the PTY LTD can be in small font)
REC:58142 (also on the front in small font)
Call Dario (back i dont want my last name on the card)
Phone: 0488157093 (back
Email: zulelectricalservices@kestrelmail.net (back)
Domestic, Commercial, Industrial, (on the back in dot points.)
Look and feel
Each slider illustrates characteristics of the customer's brand and the style your logo design should communicate.

```html
<!DOCTYPE html>
<html lang="en">
<head>
<meta charset="utf-8">
<title>Zul Electrical Services – Business Card</title>
<link href="https://fonts.googleapis.com/css2?family=Questrial&display=swap" rel="stylesheet">
<style>
  :root{
    --bg:#e9e7e3;
    --card:#ffffff;
    --card-shade:#f1f1f1;
    --green:#3fb54a;
    --green-soft:#9fd9a5;
    --grey:#6d6d6d;
    --grey-light:#8a8a8a;
  }
  *{margin:0;padding:0;box-sizing:border-box}
  html,body{width:1200px;height:1184px;overflow:hidden}
  body{background:var(--bg);font-family:"Questrial",sans-serif;position:relative}
  .card{
    position:absolute;left:150px;width:900px;height:514px;
    background:linear-gradient(100deg,var(--card) 55%,var(--card-shade));
    box-shadow:0 6px 22px rgba(0,0,0,.18);
  }
  .card--front{top:50px}
  .card--back{top:620px}

  /* brand name block */
  .brand{display:flex;align-items:center;gap:18px;color:var(--green)}
  .brand__dot{width:34px;height:34px;border-radius:50%;background:var(--green);flex:none}
  .brand__name{font-size:58px;letter-spacing:.5px;white-space:nowrap}
  .brand__suffix{font-size:20px;letter-spacing:5px;color:var(--grey)}

  .card--front .brand{position:absolute;left:120px;top:190px}
  .card--front .brand__suffix{position:absolute;left:172px;top:292px}
  .card--front .licence{position:absolute;left:172px;top:320px;font-size:16px;letter-spacing:3px;color:var(--grey-light)}

  .card--back .brand{position:absolute;left:70px;top:80px;gap:12px}
  .card--back .brand__dot{width:22px;height:22px}
  .card--back .brand__name{font-size:36px}
  .card--back .brand__suffix{position:absolute;left:104px;top:132px;font-size:14px;letter-spacing:4px}

  .sectors{position:absolute;left:640px;top:36px;list-style:none;font-size:17px;color:var(--grey);letter-spacing:1.5px;line-height:26px}
  .sectors li{display:flex;align-items:center;gap:10px}
  .sectors li::before{content:"";width:6px;height:6px;border-radius:50%;background:var(--green);flex:none}
  .sectors li:nth-child(2){padding-left:14px}
  .sectors li:nth-child(3){padding-left:28px}

  .person{position:absolute;left:80px;top:235px}
  .person__name{font-size:32px;letter-spacing:2px;color:var(--green)}
  .person__role{font-size:19px;letter-spacing:3px;color:var(--grey);margin-top:4px}

  .divider{position:absolute;left:210px;top:275px;width:620px;height:2px;background:linear-gradient(90deg,var(--green-soft),var(--green))}

  .contact{position:absolute;left:80px;top:408px;list-style:none;font-size:21px;letter-spacing:2px;color:var(--grey);line-height:34px}
  .contact li{display:flex;align-items:center;gap:14px}
  .contact svg{width:16px;height:16px;flex:none}
</style>
</head>
<body>
  <section class="card card--front">
    <div class="brand">
      <span class="brand__dot"></span>
      <span class="brand__name">Zul Electrical Services</span>
    </div>
    <div class="brand__suffix">PTY LTD</div>
    <div class="licence">REC:58142</div>
  </section>

  <section class="card card--back">
    <div class="brand">
      <span class="brand__dot"></span>
      <span class="brand__name">Zul Electrical Services</span>
    </div>
    <div class="brand__suffix">PTY LTD</div>

    <ul class="sectors">
      <li>Domestic</li>
      <li>Commercial</li>
      <li>Industrial</li>
    </ul>

    <div class="person">
      <div class="person__name">DARIO</div>
      <div class="person__role">MANAGER</div>
    </div>
    <div class="divider"></div>

    <ul class="contact">
      <li><svg viewBox="0 0 16 16"><rect x="4" y="0" width="8" height="16" rx="1.5" fill="#3fb54a"/><rect x="5.5" y="2" width="5" height="8" fill="#fff"/></svg>0488157093</li>
      <li><svg viewBox="0 0 16 16"><rect x="0" y="3" width="16" height="10" fill="#3fb54a"/><path d="M0 3l8 6 8-6" stroke="#fff" stroke-width="1.4" fill="none"/></svg>zulelectricalservices@kestrelmail.net</li>
    </ul>
  </section>
</body>
</html>
```